Simple HTML Design Needed

We're looking for a simple yet elegant HTML design that will be used for a custom wordpress theme.

We're fairly open to design ideas, but the final product will incorporate elements from the following examples:

http://www.pixorant.com/tallmotif/
http://layoutgrove.com/demo/quillwave/
http://www.polvano.at/themedemo/?theme=arbrix

We just need the homepage HTML and CSS; we'll create the rest of the pages, unless you want to go above an beyond.

The most creative design will win!

```html
<!DOCTYPE html>
<html lang="en">
<head>
<meta charset="utf-8">
<title>Studio Forma</title>
<link rel="stylesheet" href="https://fonts.googleapis.com/css2?family=Noto+Sans:wght@400;700&display=swap">
<style>
:root{
  --ink:#6b6b6b;
  --heading-grey:#7a7a7a;
  --blue:#1a73c9;
  --blue-light:#8ec9ff;
  --page:#f7f7f7;
  --card:#ffffff;
  --line:#d9d9d9;
  --top:#0d0d0d;
  --nav-text:#c9c9c9;
}
*{box-sizing:border-box;margin:0;padding:0}
html,body{width:859px;height:1200px;overflow:hidden}
body{position:relative;background:var(--page);font-family:"Noto Sans",Arial,sans-serif;color:var(--ink)}
a{color:var(--blue);text-decoration:none}
.abs{position:absolute}

.topbar{left:0;top:0;width:859px;height:32px;background:var(--top);border-bottom:1px solid #333}
.masthead{left:0;top:32px;width:859px;height:69px;background:linear-gradient(#303030,#1e1e1e);border-bottom:1px solid #444}
.brand{left:20px;top:49px;font-size:28px;font-weight:700;color:#e6e6e6;letter-spacing:1px}
.nav{top:59px;font-size:14px;color:var(--nav-text)}
.nav.current{color:#4fa9ff}

.hero{left:0;top:101px;width:859px;height:315px;background:radial-gradient(ellipse at 75% 95%,#2f6fb8 0%,#123b6e 35%,#050b16 75%,#000 100%)}
.hero-title{left:55px;top:176px;font-size:31px;color:var(--blue-light);font-weight:400}
.hero-text{left:55px;width:420px;font-size:14.2px;line-height:17px;color:#f0f0f0}
.hero-btn{left:353px;top:347px;width:108px;height:31px;border-radius:9px;background:linear-gradient(#6fb0f0,#1e5fb4);border:1px solid #9cc9f5;color:#e9f4ff;font-size:14px;text-align:center;line-height:29px;box-shadow:0 4px 6px rgba(0,0,0,.6)}
.hero-art{left:520px;top:150px;width:215px;height:240px;background:radial-gradient(ellipse at 50% 60%,rgba(70,140,215,.55) 0%,rgba(40,100,180,.25) 55%,rgba(20,60,120,0) 75%)}

.feature{top:444px;width:250px;height:119px;background:var(--card);border:1px solid var(--line);border-radius:8px;box-shadow:0 4px 6px -3px rgba(120,150,190,.35)}
.feature svg{position:absolute;left:14px;top:18px}
.feature h3{position:absolute;left:47px;top:14px;font-size:17px;font-weight:400;color:var(--blue)}
.feature p{position:absolute;left:47px;top:44px;width:190px;font-size:11px;line-height:17px;color:#8a8a8a}

.section-title{font-size:21px;font-weight:400;color:var(--heading-grey)}
.intro{left:20px;top:650px;width:540px;font-size:11px;line-height:17px;color:var(--ink)}
.intro b{color:var(--blue)}
.service h4{font-size:14.5px;font-weight:700;color:var(--blue);display:flex;align-items:center;gap:6px}
.service h4::before{content:"";width:11px;height:11px;border-radius:50%;background:var(--blue);box-shadow:inset 0 0 0 3px #5aa3ea}
.service-photo{width:248px;height:93px;border:5px solid #cfcfcf}
.service p{font-size:11px;line-height:17px;color:var(--ink);width:260px}
.more{font-size:11px;text-decoration:underline}

.post-photo{left:584px;width:108px;height:58px}
.post-text{left:705px;width:140px;font-size:10.5px;line-height:16.5px;color:var(--ink)}
.post-rule{left:584px;width:255px;height:1px;background:var(--line)}

.collection{left:20px;top:1016px;width:819px;height:167px;border:1px solid var(--line);border-radius:8px;background:linear-gradient(#ffffff,#f1f1f1);overflow:hidden}
.collection-foot{position:absolute;left:0;bottom:0;width:100%;height:33px;background:#eeeeee;border-top:1px solid var(--line)}
.thumb{top:1071px;width:167px;height:69px;border:3px solid #fff;box-shadow:0 0 0 1px #bbb}
.arrow{top:1096px;width:18px;height:18px}
</style>
</head>
<body>

<div class="abs topbar"></div>
<header class="abs masthead"></header>
<div class="abs brand">Studio Forma</div>
<nav>
  <a class="abs nav current" style="left:414px">Home</a>
  <a class="abs nav" style="left:501px">About</a>
  <a class="abs nav" style="left:589px">Portfolio</a>
  <a class="abs nav" style="left:690px">Blog</a>
  <a class="abs nav" style="left:769px">Contact</a>
</nav>

<section class="abs hero"></section>
<h1 class="abs hero-title">Lorem ipsum dolor sit amet</h1>
<p class="abs hero-text" style="top:228px">Sectetur adipisicing elit, sed do eiusmod tempor incididunt ut labore et dolore magna aliqua.</p>
<p class="abs hero-text" style="top:279px">nostrud exercitation ullamco laboris nisi ut aliquip exa com consequat. Duis aute irure dolor in reprehenderit.</p>
<a class="abs hero-btn">View All</a>
<div class="abs hero-art" role="img" aria-label="Illustration of a job seeker holding a sign reading Free for Job"></div>

<article class="abs feature" style="left:24px">
  <svg width="26" height="26" viewBox="0 0 26 26"><g fill="none" stroke="#1a73c9" stroke-width="3.5"><path d="M5 9a9 9 0 0 1 15-2"/><path d="M21 17a9 9 0 0 1-15 2"/></g><path d="M17 3l5 5-6 1z M9 23l-5-5 6-1z" fill="#1a73c9"/></svg>
  <h3>New Interaction</h3>
  <p>Adipisicing elit, sed do eiusm ode incididunt ut labore et dlore mag nostrud exerci.</p>
</article>
<article class="abs feature" style="left:305px">
  <svg width="26" height="26" viewBox="0 0 26 26"><path d="M22 9A10 10 0 1 0 23 15" fill="none" stroke="#1a73c9" stroke-width="4"/><path d="M13 13h11v4H13z" fill="#1a73c9"/></svg>
  <h3>Social Media</h3>
  <p>Mostrud exerciattion ullacom lab rure door mangae alsste formed Duis autei rure dolor in.</p>
</article>
<article class="abs feature" style="left:587px">
  <svg width="26" height="26" viewBox="0 0 26 26"><g fill="#1a73c9"><path d="M10 3h6l3 5-3 2-3-5-2 3-3-2z"/><path d="M22 14l3 5-3 5h-5v-4h3l-2-3z"/><path d="M4 24l-3-5 3-5 3 2-2 3h5v4z"/></g></svg>
  <h3>Digital Lifestyle</h3>
  <p>Emination delart ulllamco laboris fugaieat commondo conequat dui coluptate corp.</p>
</article>

<h2 class="abs section-title" style="left:20px;top:603px">Welcome to Studio Forma</h2>
<p class="abs intro"><a>Studio Forma</a> is a high quality <a>free css template</a> for your personal or commercial websites. Credit goes to <a>Open Pictures</a> for photos used in this template. Validate <b>XHTML</b> &amp; <b>CSS</b>. Ut enim ad minim veniamquis nostrud exercitation ullamco laboris nisi ut aliquip ex ea commodo consequat. Duis aute irure dolor in reprehenderit in voluptate veli</p>

<div class="abs service" style="left:20px;top:741px"><h4>Interactive Marketing</h4></div>
<div class="abs service-photo" style="left:20px;top:769px;background:linear-gradient(#1b2a66,#3a3f7a 45%,#c88a2a 70%,#0f1a3a)" role="img" aria-label="Photo of a city waterfront lit up at night"></div>
<div class="abs service" style="left:20px;top:871px"><p>Eiusmod tempor incididunt ut labore et dolore magna aliqua. Ut enim ad minim venia mquisa nostrud exercitation ullamco laboris.</p></div>
<a class="abs more" style="left:208px;top:930px">&gt;&gt; Read More</a>

<div class="abs service" style="left:302px;top:741px"><h4>Technical Consulting</h4></div>
<div class="abs service-photo" style="left:302px;top:769px;background:linear-gradient(#e9f1f8,#c6d4e0 40%,#4a6f8c 75%,#2d4a3a)" role="img" aria-label="Photo of a city skyline with tall office towers"></div>
<div class="abs service" style="left:302px;top:871px"><p>Ut enim ad minim veniamquis nostrud exercit aliquip ex ea commodo consequat. Duis autei rure dolor in reprehenderit.</p></div>
<a class="abs more" style="left:490px;top:930px">&gt;&gt; Read More</a>

<h2 class="abs section-title" style="left:583px;top:603px">Recent Posts</h2>

<div class="abs post-photo" style="top:652px;background:linear-gradient(#8fc9ea,#2fb3c9 50%,#3d6a4a)" role="img" aria-label="Photo of a coastal city by turquoise water"></div>
<p class="abs post-text" style="top:650px">Nunc varius, odio lobortis tempor mollis, sapien risus dapibus ligula...</p>
<a class="abs more" style="left:771px;top:711px">&gt;&gt; Read More</a>
<div class="abs post-rule" style="top:744px"></div>

<div class="abs post-photo" style="top:762px;background:linear-gradient(#2e4a7a,#6a5a6a 50%,#1a1e2a)" role="img" aria-label="Photo of a city skyline at dusk"></div>
<p class="abs post-text" style="top:760px">Donec aliquet, neque eget mattis lacinia, dolor mauris ultricies diam...</p>
<a class="abs more" style="left:771px;top:821px">&gt;&gt; Read More</a>
<div class="abs post-rule" style="top:854px"></div>

<div class="abs post-photo" style="top:873px;background:linear-gradient(90deg,#5a6470,#dfe4ea 50%,#5a6470)" role="img" aria-label="Photo of a skybridge between two steel towers"></div>
<p class="abs post-text" style="top:871px">Vestibulum sem urna, euismod ornare malesuada eget, vehicula id enim...</p>
<a class="abs more" style="left:771px;top:934px">&gt;&gt; Read More</a>
<div class="abs post-rule" style="top:965px"></div>

<section class="abs collection"><div class="collection-foot"></div></section>
<h2 class="abs section-title" style="left:37px;top:1032px">Old Design Collection</h2>
<svg class="abs arrow" style="left:53px" viewBox="0 0 18 18"><circle cx="9" cy="9" r="9" fill="#7d7d7d"/><path d="M11 4.5L6 9l5 4.5z" fill="#fff"/></svg>
<div class="abs thumb" style="left:85px;background:linear-gradient(90deg,#1c1416,#5a2a22 55%,#8a3a2a)" role="img" aria-label="Preview of a dark interior decoration website design"></div>
<div class="abs thumb" style="left:259px;background:linear-gradient(90deg,#2a2a2a 50%,#c8b8a0 50%)" role="img" aria-label="Preview of a dark and sand coloured car website design"></div>
<div class="abs thumb" style="left:433px;background:linear-gradient(#b8e04a,#8cc83a 70%,#f4f4f4 70%)" role="img" aria-label="Preview of a bright green automobile website design"></div>
<div class="abs thumb" style="left:607px;background:linear-gradient(#1a1a1a 40%,#f6f6f6 40%)" role="img" aria-label="Preview of a black and white corporate website design"></div>
<svg class="abs arrow" style="left:788px" viewBox="0 0 18 18"><circle cx="9" cy="9" r="9" fill="#7d7d7d"/><path d="M7 4.5L12 9l-5 4.5z" fill="#fff"/></svg>
<a class="abs more" style="left:756px;top:1157px">&gt;&gt; View More</a>

</body>
</html>
```